Flyer Template

I need a flyer template for door knocking on properties. Text Boxes need to be editable, with a header and text body. Footer to be my info. Project to be stylized to match my real estate signs and logo art from past projects

```html
<!DOCTYPE html>
<html lang="en">
<head>
<meta charset="utf-8">
<title>Brandt Realty – Door Knocking Flyer</title>
<link rel="stylesheet" href="https://fonts.googleapis.com/css2?family=Montserrat:wght@600;700;800&family=Open+Sans:wght@400;600&family=Oswald:wght@500&display=swap">
<style>
  :root{
    --brand-red:#e0000f;
    --ink:#1e1e1e;
    --paper:#ffffff;
    --photo-tone-light:#dcd8ce;
    --photo-tone-dark:#c9c4b8;
    --text-dark:#222222;
    --text-light:#ffffff;
  }
  *{box-sizing:border-box;margin:0;padding:0}
  html,body{width:671px;height:1200px;overflow:hidden;background:var(--paper)}
  body{font-family:"Open Sans",Arial,sans-serif;color:var(--text-dark)}
  .flyer{position:relative;width:671px;height:1200px;overflow:hidden}

  .top-rule{height:13px;background:var(--brand-red)}

  .masthead{position:relative;height:227px;background:var(--paper)}
  .masthead-texture{position:absolute;left:0;top:0;width:160px;height:227px;
    background:linear-gradient(90deg,#e6e6e6 0%,#f3f3f3 60%,rgba(255,255,255,0) 100%)}
  .brand{position:absolute;left:0;right:0;top:150px;display:flex;justify-content:center;align-items:center;gap:12px}
  .brand-square{width:20px;height:20px;background:var(--brand-red)}
  .brand-name{font-family:"Montserrat",Arial,sans-serif;font-weight:700;font-size:26px;letter-spacing:2px;color:#111}

  .hero-photo{height:449px;background:linear-gradient(160deg,var(--photo-tone-light) 0%,var(--photo-tone-dark) 100%)}

  .info-band{display:flex;height:202px}
  .about{width:335px;background:var(--ink);color:var(--text-light);text-align:center;padding:20px 22px 0}
  .features{flex:1;background:var(--brand-red);color:var(--text-light);padding:20px 0 0}
  .section-title{font-family:"Montserrat",Arial,sans-serif;font-weight:700;font-variant:small-caps;font-size:30px;line-height:1;letter-spacing:1px;text-align:center}
  .about-body{margin-top:16px;font-size:11px;line-height:17.5px}
  .feature-list{list-style:none;position:relative;height:140px}
  .feature{position:absolute;display:flex;align-items:center;gap:8px;font-size:11px;font-weight:600}
  .feature-icon{width:26px;height:26px;border-radius:50%;background:var(--paper);display:flex;align-items:center;justify-content:center}
  .feature-icon svg{width:14px;height:14px;fill:none;stroke:#444;stroke-width:1.6;stroke-linecap:round;stroke-linejoin:round}

  .agent{position:relative;height:218px;background:linear-gradient(90deg,#f4f4f4 0%,#ffffff 40%,#f6f6f6 100%)}
  .agent-photo{position:absolute;left:31px;top:42px;width:114px;height:114px;border-radius:50%;border:4px solid var(--paper);box-shadow:0 0 0 1px #ddd;background:linear-gradient(160deg,#b4573a 0%,#7a4032 100%)}
  .agent-name{position:absolute;left:155px;top:32px;font-family:"Montserrat",Arial,sans-serif;font-weight:700;font-size:46px;letter-spacing:2.5px;word-spacing:8px;color:var(--brand-red);line-height:1;white-space:nowrap}
  .agent-contact{position:absolute;left:155px;top:92px;display:flex;align-items:center;gap:8px;font-family:"Montserrat",Arial,sans-serif;font-weight:700;color:#111;white-space:nowrap}
  .agent-contact .phone{font-size:22px;letter-spacing:.5px}
  .agent-contact .email{font-size:18px;letter-spacing:.5px}
  .agent-contact svg{width:16px;height:16px}
  .divider{width:1px;height:24px;background:#666;margin:0 4px}
  .agent-bio{position:absolute;left:164px;top:135px;width:470px;font-size:9.4px;line-height:12.5px;color:#222}

  .footer{display:flex;height:91px}
  .footer-brokerage{width:335px;background:var(--ink);display:flex;align-items:center;justify-content:center;gap:10px}
  .brokerage-square{width:16px;height:16px;background:var(--brand-red)}
  .brokerage-name{font-family:"Oswald",Arial,sans-serif;font-weight:500;font-size:24px;color:var(--text-light);letter-spacing:.5px}
  .footer-notice{flex:1;background:var(--brand-red);display:flex;align-items:center;justify-content:center;text-align:center;font-family:"Montserrat",Arial,sans-serif;font-weight:700;font-variant:small-caps;font-size:17px;line-height:19px;color:var(--text-light);letter-spacing:.5px}
</style>
</head>
<body>
<main class="flyer">
  <div class="top-rule"></div>

  <header class="masthead">
    <div class="masthead-texture" role="img" aria-label="Soft grey halftone dot texture"></div>
    <div class="brand">
      <span class="brand-square"></span>
      <span class="brand-name">BRANDT REALTY</span>
    </div>
  </header>

  <div class="hero-photo" role="img" aria-label="Photo of a two-storey house for sale with a For Sale sign in the front yard"></div>

  <section class="info-band">
    <div class="about">
      <h2 class="section-title">About Us</h2>
      <p class="about-body">We’re #1. Holding the top spot in agent count, units and sales volume, our sales force is one to be reckoned with. Home to the Tech-Enabled Agent, our business model equips agents with a technological edge and the ability to offer customers whatever they wish.</p>
    </div>
    <div class="features">
      <h2 class="section-title">Key Features</h2>
      <ul class="feature-list">
        <li class="feature" style="left:15px;top:28px"><span class="feature-icon"><svg viewBox="0 0 16 16"><circle cx="8" cy="5" r="3"/><path d="M2.5 14c.8-3 3-4.5 5.5-4.5s4.7 1.5 5.5 4.5"/></svg></span>Work with an Agent</li>
        <li class="feature" style="left:181px;top:28px"><span class="feature-icon"><svg viewBox="0 0 16 16"><path d="M2.5 7.5 8 2.5l5.5 5"/><path d="M4 6.5V13.5h8V6.5"/></svg></span>Get Local</li>
        <li class="feature" style="left:15px;top:70px"><span class="feature-icon"><svg viewBox="0 0 16 16"><circle cx="7" cy="7" r="4.2"/><path d="m10.2 10.2 3.3 3.3"/></svg></span>Custom Searches</li>
        <li class="feature" style="left:181px;top:70px"><span class="feature-icon"><svg viewBox="0 0 16 16"><path d="M4.5 2.5h7v11L8 11l-3.5 2.5z"/></svg></span>Anytime Access</li>
        <li class="feature" style="left:15px;top:117px"><span class="feature-icon"><svg viewBox="0 0 16 16"><path d="M2 4l4-1.5 4 1.5 4-1.5v9.5l-4 1.5-4-1.5-4 1.5z"/><path d="M6 2.5v9.5M10 4v9.5"/></svg></span>Dynamic Map</li>
        <li class="feature" style="left:181px;top:117px"><span class="feature-icon"><svg viewBox="0 0 16 16"><rect x="3" y="2.5" width="10" height="11" rx="1"/><path d="M5.5 6h5M5.5 8.5h5M5.5 11h3"/></svg></span>Share Information</li>
      </ul>
    </div>
  </section>

  <section class="agent">
    <div class="agent-photo" role="img" aria-label="Portrait photo of the agent"></div>
    <h1 class="agent-name">JORDAN BRANDT</h1>
    <div class="agent-contact">
      <svg viewBox="0 0 16 16"><path d="M4 1.5 6.5 4 5 6c.8 2 2.5 3.8 5 5l2-1.5 2.5 2.5-2 2.5C7 14 2 9 1.5 3.5z" fill="#e0000f"/></svg>
      <span class="phone">907-555-0148</span>
      <span class="divider"></span>
      <svg viewBox="0 0 16 16"><rect x="1" y="3" width="14" height="10" fill="#e0000f"/><path d="M1 3l7 6 7-6M1 13l5-5M15 13l-5-5" stroke="#fff" stroke-width="1.2" fill="none"/></svg>
      <span class="email">JBRANDT@MAILBOX.COM</span>
    </div>
    <p class="agent-bio">Lorem Ipsum is simply dummy text of the printing and typesetting industry. Lorem Ipsum has been the industry's standard dummy text ever since the 1500s, when an unknown printer took a galley of type and scrambled it to make a type specimen book.</p>
  </section>

  <footer class="footer">
    <div class="footer-brokerage">
      <span class="brokerage-square"></span>
      <span class="brokerage-name">NORTHSTAR GROUP REALTY</span>
    </div>
    <div class="footer-notice">Each office independently<br>owned and Operated</div>
  </footer>
</main>
</body>
</html>
```